Amber Ridge Productions

I need a business card design for a new freelance film production company using or incorporating the logo:
I want the card to be creative, minimal, yet professional. Feel free to use a variety of different shapes and sizes/ textures for the card.

Industry/Entity Type

Film Production

```html
<!DOCTYPE html>
<html lang="en">
<head>
<meta charset="utf-8">
<title>Amber Ridge Productions – Business Card</title>
<link rel="stylesheet" href="https://fonts.googleapis.com/css2?family=Jost:wght@400;500&display=swap">
<style>
  :root {
    --backdrop: #2a2a2a;
    --brand-blue: #1160ad;
    --panel-light: #ffffff;
    --panel-shade: #dfe2e5;
    --ink-white: #ffffff;
  }
  * { margin: 0; padding: 0; box-sizing: border-box; }
  html, body {
    width: 1200px;
    height: 750px;
    overflow: hidden;
    background: var(--backdrop);
    font-family: "Jost", "Futura", sans-serif;
  }
  .canvas {
    position: relative;
    width: 1200px;
    height: 750px;
  }
  .business-card {
    position: absolute;
    left: 380px;
    top: 70px;
    width: 440px;
    height: 610px;
    border-radius: 26px;
    background: var(--brand-blue);
    overflow: hidden;
  }
  .light-panel {
    position: absolute;
    inset: 0;
    background: radial-gradient(ellipse at 45% 45%, var(--panel-light) 35%, var(--panel-shade) 100%);
    clip-path: polygon(0 24%, 71% 30%, 58% 100%, 0 100%);
  }
  .holder {
    position: absolute;
    top: 46px;
    right: 42px;
    color: var(--ink-white);
  }
  .holder-name {
    font-size: 19px;
    font-weight: 400;
    letter-spacing: 0.3px;
  }
  .holder-title {
    font-size: 10px;
    font-weight: 400;
    margin-top: 1px;
  }
  .company-name {
    position: absolute;
    left: 54px;
    top: 300px;
    width: 180px;
    display: flex;
    align-items: center;
    gap: 10px;
    color: var(--brand-blue);
    font-size: 21px;
    font-weight: 500;
    line-height: 1.15;
    letter-spacing: 1.5px;
    text-transform: uppercase;
  }
  .company-mark {
    flex: none;
    width: 14px;
    height: 14px;
    background: var(--brand-blue);
  }
  .contact-block {
    position: absolute;
    left: 306px;
    bottom: 30px;
    writing-mode: vertical-rl;
    transform: rotate(180deg);
    color: var(--ink-white);
    font-size: 11px;
    font-weight: 400;
    line-height: 1.45;
    letter-spacing: 0.4px;
    white-space: nowrap;
  }
</style>
</head>
<body>
  <main class="canvas">
    <section class="business-card">
      <div class="light-panel"></div>

      <div class="holder">
        <p class="holder-name">Daniel Hayes</p>
        <p class="holder-title">Director</p>
      </div>

      <div class="company-name">
        <span class="company-mark"></span>
        <span>Amber Ridge Productions</span>
      </div>

      <div class="contact-block">
        <p class="contact-address">412 Maple Avenue | Denver, CO, 80203</p>
        <p class="contact-lines">P: (303) 555-0147 | hello@amberridge.com</p>
      </div>
    </section>
  </main>
</body>
</html>
```